business card for KestrelLine Construction
need a tag line (here to meet your needs)?
business card for KestrelLine Construction -
Creative Brief
Simple
Lorcan Whitlaney
Foreman
New Jersey or servicing north jersey
info@Kestrel-Line.com
www.Kestrel-Line.com
fully licensed fully insured
logo. residential commercial. 24hr emergency service. specializing in: *roofs *chimneys *masonry *gutters
logo. pic of workvan with logo Notes:________________________________________________________________________________________

```html
<!DOCTYPE html>
<html lang="en">
<head>
<meta charset="utf-8">
<title>KestrelLine Construction – Business Card</title>
<link href="https://fonts.googleapis.com/css2?family=Open+Sans:ital,wght@0,400;0,600;0,700;1,700&display=swap" rel="stylesheet">
<style>
  :root {
    --navy: #2b3a8f;
    --navy-dark: #1f2b72;
    --orange: #f49a1a;
    --white: #ffffff;
    --ink: #333333;
    --grey: #8a8a8a;
    --rule: #b5b5b5;
    --backdrop: #e9e6e1;
  }
  * { box-sizing: border-box; margin: 0; padding: 0; }
  html, body { width: 1200px; height: 432px; overflow: hidden; }
  body {
    background: var(--backdrop);
    font-family: "Open Sans", Arial, sans-serif;
    position: relative;
  }
  .card {
    position: absolute;
    top: 53px;
    width: 540px;
    height: 326px;
    background: var(--white);
    border-radius: 22px;
    overflow: hidden;
    box-shadow: 0 3px 10px rgba(0,0,0,0.25);
  }
  .card--front { left: 24px; }
  .card--back { left: 634px; }

  /* front */
  .brand-name {
    position: absolute; left: 26px; top: 30px;
    font-size: 30px; font-weight: 700; color: var(--navy);
    line-height: 1.05; letter-spacing: -0.5px;
  }
  .brand-name small { display: block; font-size: 17px; letter-spacing: 2px; }
  .person {
    position: absolute; left: 26px; top: 112px;
    font-size: 19px; color: var(--navy);
  }
  .person .divider { margin: 0 8px; }
  .service-area {
    position: absolute; left: 26px; top: 156px;
    font-size: 21px; font-weight: 600; color: var(--orange);
  }
  .credentials {
    position: absolute; left: 26px; top: 190px;
    font-size: 12px; font-weight: 700; font-style: italic; color: var(--ink);
  }
  .contacts {
    position: absolute; left: 26px; top: 258px;
    display: grid; grid-template-columns: 158px 170px; row-gap: 8px;
    font-size: 12px; color: var(--ink);
  }
  .contact { display: flex; align-items: center; gap: 6px; }
  .contact svg { width: 12px; height: 12px; flex: none; }

  .panel { position: absolute; inset: 0; }
  .panel-text {
    position: absolute; right: 22px; top: 22px; width: 150px;
    text-align: right; color: var(--white); font-size: 13px; line-height: 1.35;
  }
  .panel-text .emergency { margin-top: 36px; }
  .panel-text .heading { margin-top: 30px; font-weight: 600; letter-spacing: 0.3px; }
  .specialties { list-style: none; margin-top: 8px; }
  .specialties li { color: var(--orange); font-weight: 600; margin-bottom: 10px; }
  .specialties li::after {
    content: ""; display: inline-block; width: 8px; height: 8px;
    margin-left: 8px; border-radius: 50%; background: var(--orange);
    vertical-align: middle;
  }

  /* back */
  .van-photo {
    position: absolute; left: 26px; top: 14px; width: 210px; height: 122px;
    background: radial-gradient(ellipse at 50% 55%, #f5f6f8 0%, #dfe2e8 60%, #ffffff 100%);
    border-radius: 6px;
  }
  .brand-faint {
    position: absolute; left: 262px; top: 38px;
    font-size: 30px; font-weight: 700; color: var(--navy); opacity: 0.18;
    line-height: 1.05;
  }
  .brand-faint small { display: block; font-size: 17px; letter-spacing: 2px; }
  .notes-label {
    position: absolute; left: 262px; top: 162px;
    font-size: 16px; color: var(--ink);
  }
  .notes-lines { position: absolute; left: 26px; right: 26px; top: 186px; }
  .notes-lines span { display: block; height: 22px; border-bottom: 1px solid var(--rule); }
  .website {
    position: absolute; left: 0; right: 0; bottom: 18px; text-align: center;
    font-size: 14px; letter-spacing: 3px; color: var(--grey);
  }
</style>
</head>
<body>

<section class="card card--front">
  <svg class="panel" viewBox="0 0 540 326" aria-hidden="true">
    <polygon points="352,0 540,0 540,326 388,326" fill="var(--navy)"/>
    <polygon points="344,0 352,0 388,326 380,326" fill="var(--orange)"/>
  </svg>

  <div class="brand-name">KestrelLine<small>CONSTRUCTION</small></div>
  <p class="person">Lorcan Whitlaney<span class="divider">|</span>Foreman</p>
  <p class="service-area">Servicing north jersey</p>
  <p class="credentials">FULLY LICENSED FULLY INSURED</p>

  <div class="contacts">
    <div class="contact">
      <svg viewBox="0 0 12 12"><path d="M2 1l2 0 1 3-1.5 1a6 6 0 003.5 3.5L8 7l3 1v2a1 1 0 01-1 1A9 9 0 011 2a1 1 0 011-1z" fill="var(--navy)"/></svg>
      1-888-555-0142
    </div>
    <div class="contact">
      <svg viewBox="0 0 12 12"><rect x="0.5" y="2" width="11" height="8" fill="none" stroke="var(--navy)"/><path d="M0.5 2l5.5 4.5L11.5 2" fill="none" stroke="var(--navy)"/></svg>
      info@Kestrel-Line.com
    </div>
    <div class="contact">
      <svg viewBox="0 0 12 12"><path d="M2 1l2 0 1 3-1.5 1a6 6 0 003.5 3.5L8 7l3 1v2a1 1 0 01-1 1A9 9 0 011 2a1 1 0 011-1z" fill="var(--navy)"/></svg>
      201-555-0187
    </div>
    <div class="contact">
      <svg viewBox="0 0 12 12"><circle cx="6" cy="6" r="5.5" fill="none" stroke="var(--navy)"/><path d="M0.5 6h11M6 0.5c-3 3-3 8 0 11M6 0.5c3 3 3 8 0 11" fill="none" stroke="var(--navy)"/></svg>
      www.Kestrel-Line.com
    </div>
  </div>

  <div class="panel-text">
    <p>Residential<br>Commercial</p>
    <p class="emergency">24hr emergency service</p>
    <p class="heading">SPECIALIZING IN:</p>
    <ul class="specialties">
      <li>roofs</li>
      <li>chimneys</li>
      <li>masonry</li>
      <li>gutters</li>
    </ul>
  </div>
</section>

<section class="card card--back">
  <div class="van-photo" role="img" aria-label="Photo of the white company work van bearing the company name"></div>
  <div class="brand-faint">KestrelLine<small>CONSTRUCTION</small></div>
  <p class="notes-label">Notes:</p>
  <div class="notes-lines"><span></span><span></span><span></span><span></span></div>
  <p class="website">www.Kestrel-Line.com</p>
</section>

</body>
</html>
```